Beekeeper needs box/label design for honey/CBD and other honey-related products

We need a box (or label) design for a beekeeping company in Virginia called Larkmoor Hollow Farm. Our products will include honey mixed with CBD oil and other essential oils (vanilla, lavender, etc).The box design should be scalable to include several different honey/oil products. We would like to incorporate our current farm logo into the design. Here is a link to a honey producing company with a series of products using their honey mixed with certain oils. It's a good reference of what type box/label design we would like (https://pipandwrenly.co/pages/honey).

Target Market(s)

Retail stores and consumers

Requirements
Must have
• Larkmoor Hollow Farm name and logo

```html
<!DOCTYPE html>
<html lang="en">
<head>
<meta charset="utf-8">
<title>Larkmoor Hollow Farm – Honey with CBD oil, Vanilla</title>
<link rel="stylesheet" href="https://fonts.googleapis.com/css2?family=Tinos:wght@400;700&display=swap">
<style>
  :root {
    --backdrop-top: #ee8a06;
    --backdrop-bottom: #fcaa30;
    --panel: #f4f3f1;
    --honey-soft: #e4cf91;
    --honey-pale: #efe4c2;
    --olive: #5d5f18;
    --shield-fill: #eeeeec;
  }
  * { box-sizing: border-box; margin: 0; padding: 0; }
  html, body { width: 1200px; height: 999px; overflow: hidden; }
  body {
    background: linear-gradient(180deg, var(--backdrop-top) 0%, var(--backdrop-bottom) 100%);
    font-family: "Tinos", "Times New Roman", serif;
    color: var(--olive);
    position: relative;
  }
  .box-front {
    position: absolute;
    left: 362px;
    top: 60px;
    width: 475px;
    height: 880px;
    background: var(--panel);
    overflow: hidden;
  }
  .honeycomb-field {
    position: absolute;
    inset: 0;
    background:
      radial-gradient(ellipse at 30% 25%, var(--honey-pale) 0%, transparent 55%),
      radial-gradient(ellipse at 75% 60%, var(--honey-soft) 0%, transparent 60%),
      linear-gradient(180deg, var(--honey-pale) 0%, #f1e7c8 50%, var(--honey-pale) 100%);
    opacity: 0.85;
  }
  .brand-shield {
    position: absolute;
    left: 116px;
    top: 0;
    width: 233px;
    height: 291px;
  }
  .brand-shield svg { position: absolute; inset: 0; }
  .brand-name {
    position: absolute;
    left: 0;
    right: 0;
    top: 118px;
    text-align: center;
    font-weight: 400;
    font-size: 27px;
    line-height: 1.15;
    letter-spacing: 1px;
    color: var(--olive);
  }
  .product-title {
    position: absolute;
    left: 0;
    right: 0;
    top: 345px;
    text-align: center;
    font-weight: 700;
    line-height: 1;
  }
  .product-title .main { display: block; font-size: 80px; letter-spacing: 1px; }
  .product-title .sub { display: block; font-size: 50px; margin-top: 2px; }
  .flavour-tag {
    position: absolute;
    left: 120px;
    top: 502px;
    width: 227px;
    height: 60px;
  }
  .flavour-tag svg { position: absolute; inset: 0; }
  .flavour-tag span {
    position: absolute;
    inset: 0;
    display: flex;
    align-items: center;
    justify-content: center;
    font-weight: 700;
    font-size: 38px;
    padding-top: 4px;
  }
  .molecule-diagram {
    position: absolute;
    left: 113px;
    top: 600px;
    width: 320px;
    height: 190px;
    background: rgba(225, 214, 170, 0.55);
    border-radius: 6px;
  }
</style>
</head>
<body>
  <main class="box-front">
    <div class="honeycomb-field" role="img" aria-label="Soft golden honeycomb hexagon pattern across the box"></div>

    <div class="brand-shield">
      <svg viewBox="0 0 233 291" width="233" height="291" aria-hidden="true">
        <polygon points="2,2 231,2 231,218 116.5,289 2,218" fill="var(--shield-fill)" stroke="var(--olive)" stroke-width="3"/>
      </svg>
      <p class="brand-name">Larkmoor<br>Hollow Farm</p>
    </div>

    <h1 class="product-title">
      <span class="main">HONEY</span>
      <span class="sub">with CBD oil</span>
    </h1>

    <div class="flavour-tag">
      <svg viewBox="0 0 227 60" width="227" height="60" aria-hidden="true">
        <polygon points="18,2 209,2 225,30 209,58 18,58 2,30" fill="none" stroke="var(--olive)" stroke-width="2.5"/>
      </svg>
      <span>VANILLA</span>
    </div>

    <div class="molecule-diagram" role="img" aria-label="Line drawing of the cannabinoid molecule structure"></div>
  </main>
</body>
</html>
```